依頼詳細
開設告知を病院や行政、居宅介護支援事業所に行うための簡易的なチラシの作成をお願いいたします。情報量は最低限で、雰囲気重視、まずは時期と場所をしっかりと伝えて初期段階の営業を行うためのツールを想定しています。
記載項目
別紙資料をご確認ください。
サイズ
A4
ページ数
片面
希望イメージ
シンプル 複雑
単色 カラフル
暗い 明るい
日常 高級
遊び心 厳粛
未来的 伝統的
女性的 男性的
希望する色
納品ファイル
補足説明

スタッフの投票で決めました。

大変すばらしい提案をいただきましてありがとうございました。今後もパンフレット等、様々依頼をさせていただく予定ですので、今後とも宜しくお願い致します。

```html
<!DOCTYPE html>
<html lang="ja">
<head>
<meta charset="utf-8">
<title>はなあかり 花灯 開設のお知らせ</title>
<link rel="stylesheet" href="https://fonts.googleapis.com/css2?family=Noto+Sans+JP:wght@400;500;700;900&family=Zen+Maru+Gothic:wght@500;700;900&display=swap">
<style>
  :root{
    --navy:#1f3468;
    --orange:#e8780f;
    --red:#c8343a;
    --ink:#2d3340;
    --white:#ffffff;
    --sky-top:#d7ecfa;
    --sky-mid:#f5fbff;
    --leaf:#b8d79c;
  }
  html,body{margin:0;padding:0;width:846px;height:1200px;overflow:hidden;background:var(--white);}
  .flyer{
    position:relative;width:846px;height:1200px;overflow:hidden;
    font-family:"Noto Sans JP",sans-serif;color:var(--ink);
  }
  .backdrop{
    position:absolute;inset:0;
    background:
      radial-gradient(ellipse 260px 380px at 0% 15%, rgba(140,190,110,.55), transparent 70%),
      radial-gradient(ellipse 300px 420px at 100% 20%, rgba(150,200,110,.6), transparent 70%),
      linear-gradient(to bottom,var(--sky-top) 0%,var(--sky-mid) 22%,#ffffff 45%,#f3f8ee 68%,var(--leaf) 100%);
  }
  .residents-photo{
    position:absolute;left:0;bottom:0;width:390px;height:540px;
    background:
      radial-gradient(ellipse 180px 240px at 45% 60%, rgba(210,205,195,.85), transparent 72%),
      radial-gradient(ellipse 240px 200px at 20% 20%, rgba(150,195,120,.6), transparent 70%),
      linear-gradient(to bottom, rgba(255,255,255,0), rgba(120,170,95,.55) 55%, rgba(95,145,80,.8));
  }
  .brand{position:absolute;top:78px;left:0;width:846px;text-align:center;color:var(--navy);}
  .brand-dot{width:68px;height:68px;border-radius:50%;background:var(--navy);margin:0 auto 22px;}
  .brand-type{font-size:21px;font-weight:700;letter-spacing:.08em;margin:0;}
  .brand-name{font-family:"Zen Maru Gothic",sans-serif;font-weight:900;font-size:58px;line-height:1;letter-spacing:.12em;margin:8px 0 0;}
  .brand-kanji{font-family:"Zen Maru Gothic",sans-serif;font-weight:900;font-size:30px;letter-spacing:.5em;margin:6px 0 0;padding-left:.5em;}
  .services-band{
    position:absolute;top:340px;left:57px;width:732px;height:38px;background:var(--navy);
    color:var(--white);font-size:25px;font-weight:700;text-align:center;line-height:38px;letter-spacing:.04em;
  }
  .opening{
    position:absolute;top:384px;left:0;width:846px;text-align:center;margin:0;
    color:var(--orange);font-size:62px;font-weight:900;letter-spacing:.02em;
  }
  .point{position:absolute;margin:0;}
  .point h2{color:var(--orange);font-size:23px;font-weight:700;line-height:1.35;margin:0 0 10px;}
  .point p{font-size:14px;line-height:1.65;margin:0;}
  .point-access{top:505px;left:57px;width:330px;}
  .point-staff{top:505px;left:450px;width:350px;}
  .point-fun{top:620px;left:450px;width:350px;}
  .info{position:absolute;left:395px;width:420px;}
  .label{
    display:inline-block;background:var(--orange);color:var(--white);font-size:15px;font-weight:700;
    width:72px;height:28px;line-height:28px;text-align:center;border-radius:14px;
  }
  .fees{top:740px;height:80px;}
  .fees .label{position:absolute;top:22px;left:0;}
  .fee-table{position:absolute;top:0;left:86px;border-collapse:collapse;font-size:14px;}
  .fee-table td{padding:1px 8px 1px 0;white-space:nowrap;}
  .fee-table td.amount{text-align:right;font-weight:500;}
  .fee-total{position:absolute;top:20px;left:248px;font-size:22px;font-weight:900;white-space:nowrap;}
  .fee-total small{font-size:15px;font-weight:700;}
  .access{top:830px;height:160px;}
  .access .label{position:absolute;top:28px;left:0;}
  .access-map{position:absolute;top:0;left:78px;width:342px;height:150px;background:linear-gradient(135deg,#ffffff,#eef3f8);border:1px solid #c9d3e0;box-sizing:border-box;}
  .address{
    position:absolute;top:-8px;right:0;background:var(--red);color:var(--white);
    font-size:13px;font-weight:700;line-height:1.35;padding:5px 10px;
  }
  .contact{top:1008px;height:90px;}
  .contact .label{position:absolute;top:8px;left:0;}
  .phone{
    position:absolute;top:-6px;left:80px;display:flex;align-items:center;gap:6px;
    color:var(--navy);font-size:42px;line-height:1.1;font-weight:900;white-space:nowrap;
  }
  .phone svg{flex:none;}
  .hours{position:absolute;top:46px;left:120px;margin:0;font-size:13px;white-space:nowrap;}
</style>
</head>
<body>
<div class="flyer">
  <div class="backdrop" role="img" aria-label="青空と木々の緑が広がる明るい屋外の風景"></div>
  <div class="residents-photo" role="img" aria-label="緑の中で杖をついて笑顔で並ぶ高齢のご夫婦の写真"></div>

  <header class="brand">
    <div class="brand-dot"></div>
    <p class="brand-type">住宅型有料老人ホーム</p>
    <h1 class="brand-name">はなあかり</h1>
    <p class="brand-kanji">花灯</p>
  </header>

  <div class="services-band">訪問介護事業所・通所介護事業所併設</div>
  <p class="opening">令和3年4月、開設。</p>

  <section class="point point-access">
    <h2>首都圏からのアクセス良好、<br>かつ自然豊か。</h2>
    <p>緑野自動車道朝日ICから車で3分。<br>朝日沼ふれあい公園まで徒歩1分。<br>自然豊かで落ち着いたホームです。</p>
  </section>

  <section class="point point-staff">
    <h2>理学療法士、作業療法士を配置。</h2>
    <p>機能訓練を重視し、個々の状態に合わせたリハビリで、いつまでも自分らしい生活を支えます。</p>
  </section>

  <section class="point point-fun">
    <h2>楽しみ方も、いろいろ。</h2>
    <p>シアタールーム等、余暇設備が充実しています。<br>畑・園芸スペースもありますので、認知機能向上のために様々な植物の栽培を楽しみましょう。</p>
  </section>

  <div class="info fees">
    <span class="label">費用</span>
    <table class="fee-table">
      <tr><td>家　賃</td><td class="amount">27,000円〜</td></tr>
      <tr><td>食　費</td><td class="amount">39,000円</td></tr>
      <tr><td>管理費</td><td class="amount">18,000円</td></tr>
    </table>
    <div class="fee-total"><small>合計</small> 84,000円〜</div>
  </div>

  <div class="info access">
    <span class="label">アクセス</span>
    <div class="access-map" role="img" aria-label="施設周辺の道路と最寄りICを示す簡易地図"></div>
    <div class="address">青葉県緑野市<br>朝日町1234-5</div>
  </div>

  <div class="info contact">
    <span class="label">お問合せ</span>
    <div class="phone">
      <svg width="34" height="34" viewBox="0 0 24 24" aria-hidden="true"><path fill="#1f3468" d="M6.6 10.8a15.1 15.1 0 0 0 6.6 6.6l2.2-2.2c.3-.3.7-.4 1-.2 1.1.4 2.3.6 3.6.6.6 0 1 .4 1 1V20c0 .6-.4 1-1 1C10.6 21 3 13.4 3 4c0-.6.4-1 1-1h3.5c.6 0 1 .4 1 1 0 1.3.2 2.5.6 3.6.1.3 0 .7-.2 1z"/></svg>
      <span>012-555-0147</span>
    </div>
    <p class="hours">営業時間　受付時間 09:00-18:00</p>
  </div>
</div>
</body>
</html>
```